ReadNest Learning App for Children with Dyslexia

Project Description:

We are seeking a talented UI/UX designer to create engaging and intuitive designs for Readnest, an innovative educational app designed to help children learn letters and words through a multisensory learning approach. The app aims to be particularly helpful for children with dyslexia, providing a supportive and interactive learning environment.

Key App Features & Design Requirements:

Account Creation Screen: Design a welcoming and straightforward sign-up page that allows users to register with their email or continue with Quorvix. The design should be clean, focusing on user-friendliness and accessibility, adhering to our terms of service and privacy policy.

Main Screen Design: The main screen should allocate at least 4/6 of its height to the interactive drawing area. It needs to display word prompts in both correct and scrambled orders and include options to "Show all Words," "Play all words," and a search function. The interface should be vibrant, engaging, and easy to navigate for children.

Profile Section: Create a user-friendly profile page that allows users to edit their profile image, name, username, email, links, and bio. The design should be clean and encourage user engagement.

NestStats Page: This section will display the user's learning progress, including rankings, a learning curve, and recently learned words. It should visually represent progress in a motivating and understandable way, suitable for a younger audience.

Visual and Auditory Feedback Implementation: Incorporate elements that support visual and auditory feedback, using dyslexia-friendly formats. This includes choosing appropriate colors, fonts, and auditory cues.

Accessibility and Customization Settings: Designs should include settings for adjusting visual contrast, font size, and the word list to accommodate individual preferences and needs.

Feel free to add more interactions and/or pages.

Design preferences:

Color Scheme: Use a bright, inviting color palette that stimulates learning and engagement without overwhelming the users.
Font Selection: Opt for fonts that are readable and accessible, particularly for users with dyslexia.
Icons and Graphics: Design custom icons and graphics that are cohesive with the app's theme and purpose. Illustrations should be simple, relatable, and supportive of the learning process.

Target Market(s)

Educational

Industry/Entity Type

Educational

Colors
0054AA
0677BA
7BADD7
CADEEF
E8F1F8
0094D4
00A9DD
6FCCEA
C7EBF8
E9F6FB

Requirements
Must have
• Educational app, a writing area, scoring and account management
Nice to have
• Statistics, Ranking Page, Settings and some nice visual features

```html
<!DOCTYPE html>
<html lang="en">
<head>
<meta charset="utf-8">
<title>Readnest – App Screens</title>
<link rel="stylesheet" href="https://fonts.googleapis.com/css2?family=Inter:wght@400;600&family=Hind:wght@400;500&family=League+Spartan:wght@700;800&family=Roboto:wght@400&display=swap">
<style>
  :root {
    --board: #666666;
    --screen: #ffffff;
    --green: #00a15a;
    --yellow: #ffd24c;
    --yellow-pale: #fff1c4;
    --green-pale: #c9ecd9;
    --ink: #0b0b0b;
    --muted: #7a7a7a;
    --field-line: #e3e3e3;
    --quorvix-bg: #ededed;
  }
  * { box-sizing: border-box; margin: 0; padding: 0; }
  html, body { width: 1200px; height: 837px; overflow: hidden; background: var(--board); }
  body { position: relative; font-family: "Hind", sans-serif; color: var(--ink); }

  .screen {
    position: absolute; top: 62px; width: 330px; height: 713px;
    background: var(--screen); overflow: hidden;
    box-shadow: 6px 8px 14px rgba(0,0,0,.35);
  }
  .screen--splash { left: 62px; }
  .screen--login { left: 435px; }
  .screen--main { left: 808px; }
  .abs { position: absolute; }

  /* Decorative letter fields */
  .letters-green {
    left: 0; top: 0; width: 330px; height: 300px;
    background: radial-gradient(ellipse 75% 95% at 50% 20%, #8fd6b0 0%, #c9ecd9 55%, rgba(255,255,255,0) 100%);
  }
  .letters-yellow {
    left: 0; width: 330px; bottom: 0;
    background: linear-gradient(to bottom, rgba(255,255,255,0) 0%, var(--yellow-pale) 45%, #ffe596 100%);
  }
  .band-top { left: 0; top: 0; }
  .band-bottom { left: 0; bottom: 0; }

  /* Splash */
  .splash-title {
    left: 0; width: 330px; top: 308px; text-align: center;
    font-family: "Inter", sans-serif; font-weight: 600; font-size: 56px; letter-spacing: -1px; line-height: 1;
  }
  .splash-tagline {
    left: 0; width: 330px; top: 372px; text-align: center;
    font-family: "Inter", sans-serif; font-size: 23px; line-height: 1;
  }

  /* Status bar */
  .status-time { left: 29px; top: 12px; font-family: "Inter", sans-serif; font-weight: 600; font-size: 13px; }
  .status-icons { right: 14px; top: 14px; }

  .wave { left: 0; top: 95px; }
  .home-bar { left: 106px; top: 702px; width: 118px; height: 4px; border-radius: 2px; background: var(--ink); }

  /* Login */
  .brand-title {
    left: 0; width: 330px; top: 44px; text-align: center;
    font-family: "Inter", sans-serif; font-weight: 600; font-size: 31px; letter-spacing: -.5px; line-height: 1;
  }
  .brand-tagline {
    left: 0; width: 330px; top: 79px; text-align: center;
    font-family: "Inter", sans-serif; font-size: 13px; line-height: 1;
  }
  .heading {
    left: 0; width: 330px; text-align: center;
    font-family: "League Spartan", sans-serif; font-weight: 800; line-height: 1;
  }
  .login-heading { top: 155px; font-size: 38px; letter-spacing: .5px; }
  .field {
    left: 21px; width: 288px; height: 39px;
    border: 1px solid var(--field-line); border-radius: 3px;
    padding-left: 16px; display: flex; align-items: center;
    font-size: 11.5px; color: #4d4d4d; padding-top: 2px;
  }
  .button {
    left: 21px; width: 288px; height: 38px; border-radius: 3px;
    display: flex; align-items: center; justify-content: center;
    font-family: "Hind", sans-serif; padding-top: 3px;
  }
  .button--login { top: 348px; background: var(--green); color: #fff; font-size: 18px; letter-spacing: 1.5px; }
  .button--signup { top: 396px; background: var(--yellow); color: var(--ink); font-size: 17px; font-weight: 500; letter-spacing: .5px; }
  .divider { left: 21px; width: 288px; top: 453px; display: flex; align-items: center; gap: 8px; font-family: "Roboto", sans-serif; font-size: 12px; color: var(--muted); }
  .divider::before, .divider::after { content: ""; flex: 1; height: 1px; background: #cfcfcf; }
  .button--quorvix { top: 482px; height: 35px; background: var(--quorvix-bg); font-family: "Roboto", sans-serif; font-size: 13px; gap: 7px; padding-top: 0; }
  .quorvix-dot { width: 15px; height: 15px; border-radius: 50%; background: var(--green); }
  .legal {
    left: 21px; width: 288px; top: 527px; text-align: center;
    font-family: "Roboto", sans-serif; font-size: 10.5px; line-height: 16px; color: var(--muted);
  }
  .legal strong { font-weight: 400; color: var(--ink); }

  /* Main */
  .main-heading { top: 60px; font-size: 26px; letter-spacing: .3px; }
  .menu-icon { left: 21px; top: 114px; }
  .points {
    left: 266px; top: 97px; width: 42px; height: 42px; border-radius: 50%;
    background: var(--yellow); text-align: center;
    font-family: "Inter", sans-serif; line-height: 1;
  }
  .points-value { display: block; font-size: 20px; margin-top: 7px; letter-spacing: -.5px; }
  .points-label { display: block; font-size: 6px; margin-top: 1px; }
  .drawing-area {
    left: 21px; top: 161px; width: 288px; height: 269px;
    border: 1px solid var(--field-line); border-radius: 3px; background: #fff;
    display: flex; align-items: center; justify-content: center;
    font-size: 11.5px; padding-top: 2px;
    box-shadow: 0 6px 6px -4px rgba(0,0,0,.18);
  }
  .tabs {
    left: 21px; top: 445px; width: 288px; height: 39px;
    border: 1px solid var(--yellow); border-radius: 3px; display: flex; overflow: hidden;
  }
  .tab { flex: 1; display: flex; align-items: center; justify-content: center; font-size: 11px; padding-top: 2px; }
  .tab--active { background: var(--yellow); }
  .word-tile {
    width: 90px; height: 39px; border: 1px solid var(--field-line); border-radius: 3px;
    background: #fff; display: flex; align-items: center; justify-content: center;
    font-size: 11px; padding-top: 2px;
  }
  .button--results { top: 628px; background: var(--green); color: #fff; font-size: 18px; letter-spacing: .8px; font-weight: 500; }
</style>
</head>
<body>

  <!-- Splash screen -->
  <section class="screen screen--splash">
    <div class="abs letters-green" role="img" aria-label="Scattered green A, B and C letter pattern"></div>
    <svg class="abs band-top" width="330" height="48" viewBox="0 0 330 48"><path d="M0 0H330V48Q165 -32 0 48Z" fill="var(--green)"/></svg>
    <div class="abs letters-yellow" style="top:424px" role="img" aria-label="Scattered yellow A, B and C letter pattern"></div>
    <svg class="abs band-bottom" width="330" height="60" viewBox="0 0 330 60"><path d="M0 14Q165 92 330 14V60H0Z" fill="var(--yellow)"/></svg>
    <h1 class="abs splash-title">Readnest</h1>
    <p class="abs splash-tagline">Learn letters and words</p>
  </section>

  <!-- Login screen -->
  <section class="screen screen--login">
    <span class="abs status-time">9:41</span>
    <svg class="abs status-icons" width="58" height="10" viewBox="0 0 58 10">
      <g fill="var(--ink)">
        <rect x="0" y="7" width="2.5" height="3" rx=".5"/><rect x="4" y="5" width="2.5" height="5" rx=".5"/>
        <rect x="8" y="3" width="2.5" height="7" rx=".5"/><rect x="12" y="0" width="2.5" height="10" rx=".5"/>
        <path d="M20 3.5a8 8 0 0 1 11 0l-1.2 1.3a6.2 6.2 0 0 0-8.6 0Z"/><path d="M22.3 6a4.6 4.6 0 0 1 6.4 0L25.5 9.5Z"/>
        <rect x="36" y="0.5" width="19" height="9" rx="2" fill="none" stroke="var(--ink)" stroke-width=".8"/>
        <rect x="37.5" y="2" width="16" height="6" rx="1"/><rect x="56" y="3.5" width="1.5" height="3" rx=".5"/>
      </g>
    </svg>
    <h1 class="abs brand-title">Readnest</h1>
    <p class="abs brand-tagline">Learn letters and words</p>
    <svg class="abs wave" width="330" height="46" viewBox="0 0 330 46">
      <path d="M0 0Q90 26 170 28Q70 52 0 38Z" fill="var(--yellow)"/>
      <path d="M330 0Q240 26 165 28Q260 46 330 30Z" fill="var(--green)"/>
    </svg>
    <h2 class="abs heading login-heading">LOGIN</h2>
    <div class="abs field" style="top:203px">Username</div>
    <div class="abs field" style="top:251px">Mobile Number</div>
    <div class="abs field" style="top:298px">Password</div>
    <div class="abs button button--login">LOGIN</div>
    <div class="abs button button--signup">Sign up with email</div>
    <div class="abs divider">or continue with</div>
    <div class="abs button button--quorvix"><span class="quorvix-dot"></span>Quorvix</div>
    <p class="abs legal">By clicking continue, you agree to our <strong>Terms of Service</strong><br>and <strong>Privacy Policy</strong></p>
    <div class="abs letters-yellow" style="top:565px" role="img" aria-label="Scattered yellow A, B and C letter pattern"></div>
    <svg class="abs band-bottom" width="330" height="60" viewBox="0 0 330 60"><path d="M0 14Q165 92 330 14V60H0Z" fill="var(--yellow)"/></svg>
    <div class="abs home-bar"></div>
  </section>

  <!-- Main screen -->
  <section class="screen screen--main">
    <span class="abs status-time">9:41</span>
    <svg class="abs status-icons" width="58" height="10" viewBox="0 0 58 10">
      <g fill="var(--ink)">
        <rect x="0" y="7" width="2.5" height="3" rx=".5"/><rect x="4" y="5" width="2.5" height="5" rx=".5"/>
        <rect x="8" y="3" width="2.5" height="7" rx=".5"/><rect x="12" y="0" width="2.5" height="10" rx=".5"/>
        <path d="M20 3.5a8 8 0 0 1 11 0l-1.2 1.3a6.2 6.2 0 0 0-8.6 0Z"/><path d="M22.3 6a4.6 4.6 0 0 1 6.4 0L25.5 9.5Z"/>
        <rect x="36" y="0.5" width="19" height="9" rx="2" fill="none" stroke="var(--ink)" stroke-width=".8"/>
        <rect x="37.5" y="2" width="16" height="6" rx="1"/><rect x="56" y="3.5" width="1.5" height="3" rx=".5"/>
      </g>
    </svg>
    <h1 class="abs heading main-heading">Main Screen</h1>
    <svg class="abs wave" width="330" height="46" viewBox="0 0 330 46">
      <path d="M0 0Q90 26 170 28Q70 52 0 38Z" fill="var(--yellow)"/>
      <path d="M330 0Q240 26 165 28Q260 46 330 30Z" fill="var(--green)"/>
    </svg>
    <svg class="abs menu-icon" width="18" height="14" viewBox="0 0 18 14">
      <g fill="var(--green)"><rect y="0" width="18" height="2.6"/><rect y="5.7" width="18" height="2.6"/><rect y="11.4" width="18" height="2.6"/></g>
    </svg>
    <div class="abs points"><span class="points-value">16</span><span class="points-label">POINTS</span></div>
    <div class="abs drawing-area">Drawing Area, at leasr 4/6 of height</div>
    <div class="abs tabs">
      <div class="tab">Show all Words</div>
      <div class="tab tab--active">Play all words</div>
    </div>
    <div class="abs letters-yellow" style="top:570px" role="img" aria-label="Scattered yellow A, B and C letter pattern"></div>
    <div class="abs word-tile" style="left:21px;top:493px">Word 1</div>
    <div class="abs word-tile" style="left:120px;top:493px">Word 2</div>
    <div class="abs word-tile" style="left:219px;top:493px">Word 3</div>
    <div class="abs word-tile" style="left:21px;top:540px">Word 4</div>
    <div class="abs word-tile" style="left:120px;top:540px">...</div>
    <svg class="abs band-bottom" width="330" height="60" viewBox="0 0 330 60"><path d="M0 14Q165 92 330 14V60H0Z" fill="var(--yellow)"/></svg>
    <div class="abs button button--results">SHOW ME THE RESULTS</div>
    <div class="abs home-bar"></div>
  </section>

</body>
</html>
```